Venture Ledger Podcast Cover Art

I need podcast cover art for my new podcast Venture Ledger. I will be interviewing authors of business books. I will discuss the topics and concepts that they discuss in their book. Each interview will be about 30-40 minutes long.

I expect most of the listeners of the podcast to be entrepreneurs.

To meet app specifications, the image will need to be 3000 x 3000 pixels and RGB colourspace.

Some designs I like are included here but please do not rip off these or any other podcast's design.

Target Market(s)

Entrepreneurs

Requirements
Must have
• The name Venture Ledger must be in the artwork. As well as "with Mirela Dunstan"

The design should be related to books or writing in some way. When the listener sees the design, they should know it is related to books or reading. Also the design should look good even when quite small.
Nice to have
• I would like a clean, professional design.
Should not have
• Cliches. For example a briefcase in the design.

Also, a photo with just the name of the podcast over it.

Please do not rip off another podcast's design!

```html
<!DOCTYPE html>
<html lang="en">
<head>
<meta charset="utf-8">
<title>Venture Ledger Podcast Cover</title>
<link href="https://fonts.googleapis.com/css2?family=Bebas+Neue&family=Montserrat:wght@500&display=swap" rel="stylesheet">
<style>
  :root {
    --page-bg: #d6d6d6;
    --frame: #ffffff;
    --blue-deep: #064b94;
    --blue-mid: #0a6fb6;
    --blue-light: #0d96d4;
    --ribbon-text: #0b78c0;
    --white: #ffffff;
  }
  * { margin: 0; padding: 0; box-sizing: border-box; }
  html, body {
    width: 693px;
    height: 1200px;
    overflow: hidden;
    background: var(--page-bg);
  }
  .canvas {
    position: relative;
    width: 693px;
    height: 1200px;
  }
  .cover {
    position: absolute;
    left: 46px;
    top: 300px;
    width: 600px;
    height: 600px;
    border: 7px solid var(--frame);
    box-shadow: 6px 8px 14px rgba(0, 0, 0, 0.35);
    overflow: hidden;
  }
  .cover-backdrop {
    position: absolute;
    inset: 0;
    background: radial-gradient(ellipse at 50% 48%, var(--blue-light) 0%, var(--blue-mid) 45%, var(--blue-deep) 100%);
  }
  .title-top {
    position: absolute;
    top: 22px;
    left: 0;
    right: 0;
    text-align: center;
    font-family: "Bebas Neue", "Oswald", sans-serif;
    font-weight: 400;
    font-size: 118px;
    line-height: 1;
    color: var(--white);
    letter-spacing: 1px;
  }
  .title-ribbon {
    position: absolute;
    top: 137px;
    left: 92px;
    width: 403px;
    height: 84px;
  }
  .title-ribbon svg { position: absolute; inset: 0; }
  .title-ribbon-text {
    position: absolute;
    inset: 0;
    display: flex;
    align-items: center;
    justify-content: center;
    padding-top: 6px;
    font-family: "Bebas Neue", "Oswald", sans-serif;
    font-size: 88px;
    line-height: 1;
    color: var(--ribbon-text);
  }
  .book-mark {
    position: absolute;
    top: 258px;
    left: 0;
    right: 0;
    height: 230px;
    display: flex;
    flex-direction: column;
    align-items: center;
    justify-content: center;
    gap: 18px;
  }
  .book-icon { display: block; }
  .book-mark-name {
    font-family: "Montserrat", sans-serif;
    font-weight: 500;
    font-size: 17px;
    letter-spacing: 8px;
    padding-left: 8px;
    color: var(--white);
  }
  .host-name {
    position: absolute;
    bottom: 36px;
    left: 0;
    right: 0;
    text-align: center;
    font-family: "Montserrat", sans-serif;
    font-weight: 500;
    font-size: 21px;
    letter-spacing: 10px;
    padding-left: 10px;
    color: var(--white);
    white-space: nowrap;
  }
</style>
</head>
<body>
  <main class="canvas">
    <section class="cover">
      <div class="cover-backdrop" role="img" aria-label="Soft blue photo of city office towers behind the cover text"></div>
      <h1 class="title-top">VENTURE</h1>
      <div class="title-ribbon">
        <svg viewBox="0 0 403 84" width="403" height="84" aria-hidden="true">
          <polygon points="0,0 403,0 364,42 403,84 0,84 39,42" fill="#ffffff"/>
        </svg>
        <span class="title-ribbon-text">LEDGER</span>
      </div>
      <div class="book-mark">
        <svg class="book-icon" viewBox="0 0 220 140" width="220" height="140" aria-hidden="true">
          <g fill="none" stroke="#ffffff" stroke-width="9" stroke-linejoin="round" stroke-linecap="round">
            <path d="M110 28 C86 12 46 10 14 18 V122 C46 114 86 116 110 132 Z"/>
            <path d="M110 28 C134 12 174 10 206 18 V122 C174 114 134 116 110 132 Z"/>
          </g>
          <g stroke="#ffffff" stroke-width="4" stroke-linecap="round" opacity="0.85">
            <line x1="36" y1="44" x2="92" y2="48"/>
            <line x1="36" y1="64" x2="92" y2="68"/>
            <line x1="36" y1="84" x2="92" y2="88"/>
            <line x1="128" y1="48" x2="184" y2="44"/>
            <line x1="128" y1="68" x2="184" y2="64"/>
            <line x1="128" y1="88" x2="184" y2="84"/>
          </g>
        </svg>
        <span class="book-mark-name">VENTURE LEDGER</span>
      </div>
      <p class="host-name">WITH MIRELA DUNSTAN</p>
    </section>
  </main>
</body>
</html>
```